Premium stylish simple clever card design for high end construction company.

I need a business card designed that is a standard size and shape (square edges) that is black in colour, with black edges. All text is to be either grey/silver or yellow/gold. On the front I want the logo (supplied as attachment g5) to be embossed or raised to give a texture. I also want the name of my company "The Quiet Ember (larger font) construction co. (smaller font)" I like the clean style (found in attachment 56419286) of the black background with silver text. But the triangle is to be gold/yellow.

On the back needs to have my contact details. In silver or gold text.

Marcus Delby - Builder
Marcus@thequietember.com.au
www.thequietember.com.au
0438201965
Lic 517904k
PO BOX 758 Wrenhaven NSW 2188

Must look simple, elegant and precise.

My work is of the utmost quality and my business card needs to project that. It needs to be simple and precise. It should scream luxury and confidence. Feel free to get creative with the font and font size. If you google "The Quiet Ember" you will see it has links to great architecture, art, nature and the fibonacci sequence so i am open to using these ideas also.

Target Market(s)

High End home owners. 30-70 year olds.

Industry/Entity Type

Residential Construction

Contact Information for Business Card

Logo and company name on front. Contact details on back.

Font styles to use
Serif
Sans Serif

Colors
ffcf3e

Requirements
Must have
• black background
Nice to have
• debossed logo (silver and gold)
• debased company name (silver)
Should not have
• It should not look like a standard construction business card with pictures of hammers or tools etc.

```html
<!DOCTYPE html>
<html lang="en">
<head>
<meta charset="utf-8">
<title>The Quiet Ember Construction Co. – Business Cards</title>
<link rel="stylesheet" href="https://fonts.googleapis.com/css2?family=Questrial&family=Jost:wght@600;700&display=swap">
<style>
  :root {
    --backdrop: #ece8e2;
    --card-black: #231f20;
    --card-white: #ffffff;
    --silver-light: #e6e7e8;
    --silver: #b9babc;
    --silver-dark: #8a8b8d;
    --text-grey: #6d6e70;
    --gold-light: #ffcf3e;
    --gold: #d8a92a;
    --gold-dark: #a97a14;
    --shadow: rgba(0, 0, 0, 0.35);
  }
  * { box-sizing: border-box; margin: 0; padding: 0; }
  html, body {
    width: 1200px;
    height: 1000px;
    overflow: hidden;
    background: var(--backdrop);
  }
  .canvas {
    position: relative;
    width: 1200px;
    height: 1000px;
  }
  .card {
    position: absolute;
    width: 350px;
    height: 200px;
    box-shadow: 0 8px 14px var(--shadow);
  }
  .card--front { background: var(--card-black); }
  .card--back-light { background: var(--card-white); }
  .card--back-dark { background: var(--card-black); }

  .front-one { left: 167px; top: 87px; }
  .back-light { left: 167px; top: 345px; }
  .front-two { left: 684px; top: 420px; }
  .back-dark { left: 684px; top: 680px; }

  /* Front */
  .brand {
    position: absolute;
    inset: 0;
    display: flex;
    flex-direction: column;
    align-items: center;
  }
  .brand__mark {
    margin-top: 28px;
    width: 86px;
    height: 86px;
    border-radius: 50%;
    background: var(--silver);
  }
  .brand__name {
    margin-top: 12px;
    font-family: "Questrial", sans-serif;
    font-size: 28px;
    letter-spacing: 0.5px;
    color: var(--silver);
    line-height: 1;
    white-space: nowrap;
  }
  .brand__tagline {
    display: flex;
    align-items: center;
    gap: 6px;
    width: 298px;
    margin-top: 3px;
    font-family: "Questrial", sans-serif;
    font-size: 10px;
    color: var(--silver);
    white-space: nowrap;
  }
  .brand__rule {
    flex: 1;
    height: 2px;
    background: var(--silver);
  }

  /* Back */
  .contact {
    position: absolute;
    inset: 0;
    padding-top: 20px;
    text-align: center;
    font-family: "Questrial", sans-serif;
  }
  .contact__name {
    font-family: "Jost", sans-serif;
    font-weight: 700;
    font-size: 21px;
    letter-spacing: 0.5px;
    line-height: 1;
    background: linear-gradient(180deg, var(--gold-light), var(--gold) 55%, var(--gold-dark));
    -webkit-background-clip: text;
    background-clip: text;
    color: transparent;
  }
  .contact__role {
    font-size: 13px;
    line-height: 1.1;
    color: var(--gold);
  }
  .contact__licence {
    font-size: 8px;
    color: var(--text-grey);
    line-height: 1.2;
  }
  .contact__web {
    margin-top: 22px;
    font-size: 19px;
    line-height: 1.1;
  }
  .contact__detail {
    font-size: 14px;
    line-height: 1.25;
  }
  .contact__gap { margin-top: 8px; }

  .card--back-light .contact__web,
  .card--back-light .contact__detail { color: var(--text-grey); }
  .card--back-dark .contact__web,
  .card--back-dark .contact__detail { color: var(--silver); }
  .card--back-dark .contact__licence { color: var(--silver-dark); }
</style>
</head>
<body>
<main class="canvas">

  <section class="card card--front front-one" aria-label="Card front">
    <div class="brand">
      <div class="brand__mark"></div>
      <p class="brand__name">THE QUIET EMBER</p>
      <p class="brand__tagline"><span class="brand__rule"></span>CONSTRUCTION CO.<span class="brand__rule"></span></p>
    </div>
  </section>

  <section class="card card--back-light back-light" aria-label="Card back, light">
    <div class="contact">
      <p class="contact__name">MARCUS DELBY</p>
      <p class="contact__role">Builder</p>
      <p class="contact__licence">Lic 517904k</p>
      <p class="contact__web">www.thequietember.com.au</p>
      <p class="contact__detail contact__gap">Marcus@thequietember.com.au</p>
      <p class="contact__detail">0438201965</p>
      <p class="contact__detail contact__gap">PO BOX 758 Wrenhaven NSW 2188</p>
    </div>
  </section>

  <section class="card card--front front-two" aria-label="Card front">
    <div class="brand">
      <div class="brand__mark"></div>
      <p class="brand__name">THE QUIET EMBER</p>
      <p class="brand__tagline"><span class="brand__rule"></span>CONSTRUCTION CO.<span class="brand__rule"></span></p>
    </div>
  </section>

  <section class="card card--back-dark back-dark" aria-label="Card back, dark">
    <div class="contact">
      <p class="contact__name">MARCUS DELBY</p>
      <p class="contact__role">Builder</p>
      <p class="contact__licence">Lic 517904k</p>
      <p class="contact__web">www.thequietember.com.au</p>
      <p class="contact__detail contact__gap">Marcus@thequietember.com.au</p>
      <p class="contact__detail">0438201965</p>
      <p class="contact__detail contact__gap">PO BOX 758 Wrenhaven NSW 2188</p>
    </div>
  </section>

</main>
</body>
</html>
```